Online Home Automation business needs business card design

New business starting up that sells home-automation products in Australia. Business card needs to look very polished and professional. The business name is "Finch Automation".
Updates

Thank you all for the great designs, We are really impressed. We are in the process of deciding on a design but keep the designs coming in.

Industry/Entity Type

Business

```html
<!DOCTYPE html>
<html lang="en">
<head>
<meta charset="utf-8">
<title>Finch Automation – Business Card</title>
<link rel="stylesheet" href="https://fonts.googleapis.com/css2?family=Open+Sans:wght@300;400;600;700&display=swap">
<style>
  :root {
    --bg: #e9e7e4;
    --card-white: #ffffff;
    --card-black: #050505;
    --card-black-glow: #262626;
    --ink: #111111;
    --ink-soft: #555555;
    --ink-mid: #333333;
    --accent: #d9262e;
    --on-dark: #ffffff;
  }
  * { margin: 0; padding: 0; box-sizing: border-box; }
  html, body { width: 1200px; height: 900px; overflow: hidden; }
  body {
    background: var(--bg);
    font-family: "Open Sans", Arial, sans-serif;
    position: relative;
  }
  .card {
    position: absolute;
    width: 600px;
    height: 343px;
    border-radius: 4px;
    box-shadow: 0 10px 28px rgba(0,0,0,0.18);
    overflow: hidden;
  }
  /* Front (dark) */
  .card-front {
    left: 300px;
    top: 60px;
    background: radial-gradient(circle at 40% 38%, var(--card-black-glow) 0%, var(--card-black) 55%);
  }
  .front-name {
    position: absolute;
    left: 210px;
    top: 110px;
    width: 360px;
    height: 140px;
    color: var(--on-dark);
    line-height: 1.05;
    transform: rotate(-25deg);
    transform-origin: center;
  }
  .front-name .line-1 { display: block; font-size: 60px; font-weight: 700; padding-left: 50px; }
  .front-name .line-2 { display: block; font-size: 60px; font-weight: 300; }

  /* Back (white) */
  .card-back {
    left: 300px;
    top: 497px;
    background: var(--card-white);
  }
  .brand {
    position: absolute;
    left: 28px;
    top: 120px;
    display: flex;
    align-items: center;
    gap: 14px;
  }
  .brand-dot {
    width: 96px; height: 96px;
    border-radius: 50%;
    background: var(--accent);
    flex: none;
  }
  .brand-name {
    color: var(--ink);
    font-size: 31px;
    line-height: 1.15;
  }
  .brand-name .bold { display: block; font-weight: 700; }
  .brand-name .regular { display: block; font-weight: 400; }
  .divider {
    position: absolute;
    left: 318px;
    top: 50px;
    width: 2px;
    height: 150px;
    background: linear-gradient(to bottom, rgba(217,38,46,0), var(--accent) 50%, rgba(217,38,46,0));
  }
  .details {
    position: absolute;
    left: 336px;
    top: 38px;
    color: var(--ink-mid);
  }
  .person-name { font-size: 22px; font-weight: 700; color: var(--ink); line-height: 1.1; }
  .person-title { font-size: 13px; color: var(--ink-soft); margin-bottom: 14px; }
  .address { font-size: 14px; line-height: 1.35; margin-bottom: 12px; }
  .contact-list { list-style: none; font-size: 14.5px; line-height: 1.5; }
  .contact-list li { display: flex; align-items: center; gap: 8px; }
  .contact-list svg { width: 13px; height: 13px; fill: var(--ink); flex: none; }
</style>
</head>
<body>

  <section class="card card-front" aria-label="Card front">
    <h1 class="front-name">
      <span class="line-1">Finch</span>
      <span class="line-2">Automation</span>
    </h1>
  </section>

  <section class="card card-back" aria-label="Card back">
    <div class="brand">
      <div class="brand-dot"></div>
      <div class="brand-name"><span class="bold">Finch</span><span class="regular">Automation</span></div>
    </div>

    <div class="divider"></div>

    <div class="details">
      <p class="person-name">Daniel R. Hale</p>
      <p class="person-title">Managing Member</p>
      <p class="address">2280 Harbour Lane,<br>Brookvale, CA 95870</p>
      <ul class="contact-list">
        <li>
          <svg viewBox="0 0 16 16" aria-hidden="true"><path d="M3.6 1.2l2.3 2.6-1.3 2a9 9 0 0 0 5.6 5.6l2-1.3 2.6 2.3-1.4 2.2C7.6 16 0 8.4 1.4 2.6z"/></svg>
          (555) 204-3810
        </li>
        <li>
          <svg viewBox="0 0 16 16" aria-hidden="true"><rect x="4" y="1" width="8" height="5"/><rect x="1" y="6" width="14" height="7" rx="1"/><rect x="4" y="11" width="8" height="4"/></svg>
          (555) 204-3811
        </li>
        <li>
          <svg viewBox="0 0 16 16" aria-hidden="true"><path d="M4 0h8a1 1 0 0 1 1 1v14a1 1 0 0 1-1 1H4a1 1 0 0 1-1-1V1a1 1 0 0 1 1-1zm1 2v10h6V2z"/></svg>
          (555) 718-4492
        </li>
        <li>
          <svg viewBox="0 0 16 16" aria-hidden="true"><path d="M1 3h14v10H1z M1 3l7 6 7-6" stroke="#fff" stroke-width="1"/></svg>
          daniel@harbourlanedev.com
        </li>
        <li>
          <svg viewBox="0 0 16 16" aria-hidden="true"><circle cx="8" cy="8" r="7"/><path d="M1 8h14M8 1c3 3 3 11 0 14M8 1c-3 3-3 11 0 14" stroke="#fff" stroke-width="1" fill="none"/></svg>
          www.harbourlanedev.com
        </li>
      </ul>
    </div>
  </section>

</body>
</html>
```